New Business Card Design for Business Consulting Business

We need a business card design that reflects the simplicity of our business. We partner with our clients to help them deliver change. We are a different kind of business consulting group. We don't just provide you with the theory. We provide you with the leadership and capability to execute change.

Vendora is a professional services organisation that partners with their clients to lead the execution of strategic process and system improvement initiatives. Vendora combines hands on delivery with coaching in best practice methodologies and approaches to build their clients capabilities to ensure their ongoing success in project implementations. Vendora offers business advisory services in Project Management, Business Process Management, Change Management and Business Analytics.

Reason: Hi Designers, Thanks for all of your great designs. There are some really creative and cool ideas. Everyone is really capturing the essence of my business Vendora. I am extending the deadline for the business card design by 6 days as I need to consult my Marketing colleague who won't be back in Australia until Wednesday. I would like to sit down with them and review all of the best designs. The key themes of the things I have really liked on my first review are: 1) Capturing the company website on the back of the card. 2) Including the company logo on the back of the card too. 3) Including the types of services on the back of the card that the company offers - Project Management - Business Process Management - Change Management - Business Analytics 4) Utilising some images on the back of the card Just so everyone knows the colour palette for the Vendora company logo is: R: 0 G: 86 B: 162 or C: 97% M: 73% Y: 4% K: 0% Thanks Gerald

Hi Designers,

Thanks for all of your submissions to date.  I am working through each design and will provide feedback on all the great work.

One thing I would like to ask is if you could submit a version that has my academic credentials under or after my name.  I am not a big fan of doing this but as I am in business consulting it does seem to be quite common.

I hold a Bachelor of Commerce (BCom) and a Master of Business Administration (MBA)

Thanks

Gerald

Hi Designers,

Thanks for all of your fantastic designs.  There are some really great designs here for my business.  I am still in the process of reviewing designs and should have this completed by tomorrow.  Some of the things I have learnt from this round of designs are:

1) I prefer to have the card without my academic qualifications

2) I really like cards that have a blue back

3) I prefer to have my name and title either left or right of centre

I hope this helps and I will endeavour to get through all of the designs tomorrow

Cheers

Gerald

Target Market(s)

We target large corporate organisations

Industry/Entity Type

Leadership

Requirements
Must have
• Must have the following business details

Gerald Huxton - Director
Address: Level 7, 82 Fernhill Road, Melbourne, Australia, 3000
Phone: +61 3 527 481 903
Fax: +61 3 9254 3718
Email: gerald.huxton@vendora-example.com.au
LinkedIn: au.linkedin.com/in/geraldphuxton/
Twiiter: @geraldphuxton
Website: www.vendora-example.com.au

```html
<!DOCTYPE html>
<html lang="en">
<head>
<meta charset="utf-8">
<title>Vendora Business Card</title>
<link rel="stylesheet" href="https://fonts.googleapis.com/css2?family=Open+Sans:wght@400;600&display=swap">
<style>
  :root {
    --brand-blue: #0a56a2;
    --card-white: #ffffff;
    --ink: #111111;
    --backdrop: #e4e5e6;
  }
  * { margin: 0; padding: 0; box-sizing: border-box; }
  html, body { width: 1200px; height: 1000px; overflow: hidden; }
  body {
    background: var(--backdrop);
    font-family: "Open Sans", sans-serif;
    position: relative;
  }
  .card {
    position: absolute;
    width: 566px;
    height: 297px;
    overflow: hidden;
  }
  .card-back {
    left: 305px;
    top: 203px;
    background: var(--brand-blue);
  }
  .brand-lockup {
    position: absolute;
    left: 0;
    right: 0;
    top: 88px;
    text-align: center;
  }
  .brand-block {
    position: relative;
    display: inline-block;
  }
  .brand-name {
    display: block;
    color: var(--card-white);
    font-size: 84px;
    font-weight: 400;
    letter-spacing: 3px;
    line-height: 1;
  }
  .brand-suffix {
    position: absolute;
    right: 0;
    top: 92px;
    color: var(--card-white);
    font-size: 12px;
    letter-spacing: 1px;
  }
  .card-front {
    left: 560px;
    top: 470px;
    background: var(--card-white);
    box-shadow: 0 6px 18px rgba(0, 0, 0, 0.25);
  }
  .front-shapes { position: absolute; inset: 0; }
  .holder-name {
    position: absolute;
    right: 24px;
    top: 78px;
    font-size: 19px;
    color: var(--ink);
  }
  .contact-list {
    position: absolute;
    left: 88px;
    top: 140px;
    list-style: none;
    font-size: 12.5px;
    line-height: 16px;
    color: var(--ink);
  }
  .website {
    position: absolute;
    right: 24px;
    bottom: 4px;
    color: var(--card-white);
    font-size: 20px;
  }
</style>
</head>
<body>
  <section class="card card-back" aria-label="Card back">
    <div class="brand-lockup">
      <div class="brand-block">
        <span class="brand-name">Vendora</span>
        <span class="brand-suffix">Pty Ltd</span>
      </div>
    </div>
  </section>

  <section class="card card-front" aria-label="Card front">
    <svg class="front-shapes" width="566" height="297" viewBox="0 0 566 297">
      <rect class="side-band" x="0" y="0" width="62" height="297" fill="var(--brand-blue)"/>
      <polygon class="footer-band" points="210,297 250,262 566,262 566,297" fill="var(--brand-blue)"/>
    </svg>
    <p class="holder-name">Gerald Huxton - Director</p>
    <ul class="contact-list">
      <li>Phone: +61 3 527 481 903</li>
      <li>Address: Level 7, 82 Fernhill Road, Melbourne, Australia, 3000</li>
      <li>Fax: +61 3 9254 3718</li>
      <li>Email: gerald.huxton@vendora-example.com.au</li>
      <li>LinkedIn: au.linkedin.com/in/geraldphuxton/</li>
      <li>Twiiter: @geraldphuxton</li>
    </ul>
    <p class="website">www.vendora-example.com.au</p>
  </section>
</body>
</html>
```